Modern Label for Loose Tea pouches on 4.5x6 Label

We need a new label for our teas that is very simple in design, but stylish and modern. This will be used to print labels for our loose tea pouches. The label will be at max 4.5x6 inches in size. There should be a place for the tea name, description, ingredients, and size that is changeable.
Preferably an AI file that allows me to setup variables to change the above items. There will also need to be our logo which is supplied, and our address on the label.
Address:
Brevo Leaf
846 Lower Maple Lane
Fairview, NY 12617
Target Market(s)
Tea Lovers
Requirements
Must have
- Adobe Illustrator file with variables setup for replacement of tea name, description, ingredients, and size (weights 2oz, 4oz, 8oz, 1lb)

```html
<!DOCTYPE html>
<html lang="en">
<head>
<meta charset="utf-8">
<title>Brevo Leaf – Green Tea Tropical Label</title>
<link rel="stylesheet" href="https://fonts.googleapis.com/css2?family=Raleway:wght@300;400&family=Tinos:ital@0;1&display=swap">
<style>
  :root {
    --paper: #ffffff;
    --charcoal: #4d4b4b;
    --ink: #2b2b2b;
    --rule: #3a3a3a;
  }
  html, body {
    margin: 0;
    padding: 0;
    overflow: hidden;
    background: var(--paper);
  }
  .label {
    position: relative;
    width: 988px;
    height: 1200px;
    background: var(--paper);
    overflow: hidden;
    color: var(--ink);
  }
  .label__swoosh {
    position: absolute;
    inset: 0;
  }
  .brand-seal {
    position: absolute;
    left: 24px;
    top: 170px;
    width: 290px;
    height: 290px;
    border-radius: 50%;
    background: var(--paper);
    display: flex;
    align-items: center;
    justify-content: center;
  }
  .brand-seal__name {
    font-family: "Raleway", sans-serif;
    font-weight: 300;
    font-size: 40px;
    letter-spacing: 0.06em;
    color: var(--ink);
    white-space: nowrap;
  }
  .pack-size {
    position: absolute;
    right: 30px;
    top: 168px;
    margin: 0;
    font-family: "Raleway", sans-serif;
    font-weight: 400;
    font-size: 36px;
    letter-spacing: 0.2em;
    line-height: 1;
  }
  .rule {
    position: absolute;
    left: 440px;
    right: 0;
    height: 3px;
    background: var(--rule);
  }
  .rule--top { top: 224px; }
  .rule--bottom { top: 956px; }
  .tea-name {
    position: absolute;
    left: 443px;
    top: 248px;
    margin: 0;
    font-family: "Raleway", sans-serif;
    font-weight: 300;
    font-size: 62px;
    line-height: 84px;
    letter-spacing: 0.12em;
    color: var(--ink);
    text-transform: uppercase;
  }
  .field-label {
    position: absolute;
    margin: 0;
    font-family: "Tinos", serif;
    font-style: italic;
    font-weight: 400;
    font-size: 38px;
    letter-spacing: 0.95em;
    line-height: 1;
    white-space: nowrap;
  }
  .field-label--description { left: 372px; top: 540px; }
  .field-label--ingredients { left: 330px; top: 746px; }
  .address {
    position: absolute;
    right: 22px;
    top: 996px;
    margin: 0;
    font-family: "Tinos", serif;
    font-style: normal;
    font-size: 34px;
    line-height: 60px;
    letter-spacing: 0.1em;
    text-align: right;
  }
</style>
</head>
<body>
  <main class="label">
    <svg class="label__swoosh" width="988" height="1200" viewBox="0 0 988 1200" aria-hidden="true">
      <path d="M0 0 L182 0 C 330 80, 450 250, 410 430 C 370 590, 190 700, 0 752 Z" fill="var(--charcoal)"/>
    </svg>

    <div class="brand-seal">
      <span class="brand-seal__name">Brevo Leaf</span>
    </div>

    <p class="pack-size">100g/5oz</p>
    <div class="rule rule--top"></div>

    <h1 class="tea-name">Green Tea<br>Tropical</h1>

    <p class="field-label field-label--description">Description</p>
    <p class="field-label field-label--ingredients">Ingredients</p>

    <div class="rule rule--bottom"></div>

    <address class="address">
      Brevo Leaf<br>
      846 Lower Maple Lane<br>
      Fairview, NY 12617
    </address>
  </main>
</body>
</html>
```